Q7 Strata needs an A4 folding brochure

We need a new 3-page, A4 folding brochure for Q7 Strata, an expansion of Q7 Engineering Pty Ltd (www.q7engineering-demo.com.au).

We provide high quality professional services for the Australian space industry. Our clients include the Marendi Launch Bureau and companies working in the space industry. We identify people with space related skills both locally and internationally who are then contracted by clients to create products and support space launch activities.

We would like the brochure to be based on an A4 page (landscape, folded into 3 sections) and look technical with a particular focus on communications systems, satellites, launchpad technology, space situational awareness, and Internet-of-Things (IoT) technology being developed within the space industry. The brochure will be provided to potential space customers and should be professional, visually appealing, clear, and uncluttered.

Include the Q7 Strata logo and the Q7 Strata heading (both are attached)

Include pictures (Australian preferred) of mission control centres, rockets, satellites, radio communications equipment, large satellite dishes, night landscapes with stars, or pictures of Australia or Earth from space. Include both graphics and photos. No cartoons or space shuttles from the 1980s please. Images should be current rather than old.

Include text from the attached ‘Q7 Strata – brochure text’ file.

We would like the colours to match the Q7 Strata logo, using mainly: navy blue (#000080) and matching blues; platinum (#E5E4E2), rocket metallic (#8A7F8D) and similar greys; black (#000000), and white (#FFFFFF). Sunlight colours may be included sparingly as a highlight.

Attached files:
- I have attached the Q7 Strata logo which must appear on the brochure (‘q7strata.ai’)
- I have attached the Q7 Strata heading, which should also appear on the brochure (‘q7strata-heading.psd’)
- I have attached the text that must be included on the brochure. Please divide this over the pages according to how it is group on the attached document. (‘Q7 Strata – brochure text’)

The following organisation logos are also attached, to be included on the brochure:
- Korvath Aerotech Guild - Member (‘KAG_member_logo_72’)
- Marendi Launch Bureau – Supplier (‘MLBSupplier’)
- Brellin Frontier Society Inc. (‘BFS_160x160’)

Target Market(s)

Our clients include the Marendi Launch Bureau and companies working in the space industry within Australia and internationally.

Requirements
Must have
• Refer to specifications in the project description above.
Nice to have
Should not have

```html
<!DOCTYPE html>
<html lang="en">
<head>
<meta charset="utf-8">
<title>Q7 Strata – Brochure Inside Spread</title>
<link href="https://fonts.googleapis.com/css2?family=Lato:wght@300;400;700;900&display=swap" rel="stylesheet">
<style>
  :root {
    --navy: #1f2466;
    --navy-deep: #171b52;
    --navy-soft: #2c3278;
    --ink: #1d1f2b;
    --paper: #ffffff;
    --canvas: #ececec;
    --platinum: #e5e4e2;
    --metal: #8a7f8d;
    --sky: #9db6d3;
    --sky-dark: #1d3a5c;
  }
  * { box-sizing: border-box; margin: 0; padding: 0; }
  html, body {
    width: 1200px; height: 800px; overflow: hidden;
    background: var(--canvas);
    font-family: "Lato", sans-serif;
  }
  .spread {
    position: absolute; left: 36px; top: 40px;
    width: 1128px; height: 720px;
    background: var(--paper);
    box-shadow: 0 10px 30px rgba(0,0,0,0.18);
    overflow: hidden;
  }
  .panel-fold {
    position: absolute; top: 0; width: 1px; height: 100%;
    background: rgba(0,0,0,0.06);
  }
  .spread-art { position: absolute; left: 376px; top: 0; }
  .capabilities {
    position: absolute; left: 40px; top: 34px; width: 304px;
    display: flex; flex-direction: column; gap: 9px;
  }
  .capability {
    border-left: 2px solid var(--navy);
    padding-left: 10px;
    font-size: 12px; line-height: 15px;
    color: var(--ink);
    text-align: justify;
  }
  .recruit-heading {
    position: absolute; left: 404px; top: 34px; width: 690px;
    color: #fff; font-weight: 700; font-size: 22px; line-height: 29px;
  }
  .recruit-rule {
    position: absolute; left: 792px; top: 100px; width: 300px; height: 1px;
    background: rgba(255,255,255,0.7);
  }
  .recruit-body {
    position: absolute; left: 404px; top: 124px; width: 318px;
    color: #e6e7f2; font-size: 11.5px; line-height: 15px;
    display: flex; flex-direction: column; gap: 12px;
  }
  .mission {
    position: absolute; left: 784px; top: 118px; width: 310px;
    color: #e6e7f2; font-size: 11.5px; line-height: 15px;
    display: flex; flex-direction: column; gap: 12px;
  }
  .mission-email { font-weight: 700; font-size: 14px; color: #fff; }
  .tagline {
    position: absolute; left: 64px; top: 612px;
    color: var(--navy); font-size: 38px; line-height: 44px;
  }
  .tagline-light { display: block; font-weight: 400; }
  .tagline-bold { display: block; font-weight: 900; }
  .base-band {
    position: absolute; left: 0; bottom: 0; width: 100%; height: 7px;
    background: var(--navy);
  }
</style>
</head>
<body>
<main class="spread">
  <div class="panel-fold" style="left:376px"></div>
  <div class="panel-fold" style="left:752px"></div>

  <svg class="spread-art" width="752" height="720" viewBox="0 0 752 720" aria-hidden="false">
    <defs>
      <linearGradient id="rocketTone" x1="0" y1="0" x2="0" y2="1">
        <stop offset="0" stop-color="#0f1e38"/>
        <stop offset="0.5" stop-color="#2a4f7a"/>
        <stop offset="1" stop-color="#8ea3b8"/>
      </linearGradient>
      <linearGradient id="towerTone" x1="0" y1="0" x2="0" y2="1">
        <stop offset="0" stop-color="#a9c1dc"/>
        <stop offset="0.7" stop-color="#b8c6d2"/>
        <stop offset="1" stop-color="#b39c74"/>
      </linearGradient>
    </defs>
    <path d="M0 0 H752 V470 C720 500 700 560 690 600 H372 C300 600 240 560 200 540 C120 520 60 600 0 640 Z" fill="var(--navy)"/>
    <g fill="#2a3080" opacity="0.55">
      <path d="M590 240 l10 28 30 2 -24 18 9 29 -25 -17 -25 17 9 -29 -24 -18 30 -2z"/>
      <path d="M680 250 l12 34 36 2 -28 22 10 34 -30 -20 -30 20 10 -34 -28 -22 36 -2z"/>
    </g>
    <path d="M512 322 q2 10 10 12 q-8 2 -10 12 q-2 -10 -10 -12 q8 -2 10 -12z" fill="#fff"/>
    <path d="M538 316 q3 15 14 18 q-11 3 -14 18 q-3 -15 -14 -18 q11 -3 14 -18z" fill="#fff"/>

    <ellipse cx="204" cy="466" rx="176" ry="164" fill="var(--navy-deep)"/>
    <ellipse cx="204" cy="466" rx="158" ry="148" fill="#fff"/>
    <ellipse cx="204" cy="466" rx="150" ry="140" fill="url(#rocketTone)" role="img" aria-label="Photo of a launch vehicle standing on its launch platform against a dark blue sky"/>

    <ellipse cx="546" cy="460" rx="170" ry="158" fill="var(--navy-deep)"/>
    <ellipse cx="546" cy="460" rx="150" ry="142" fill="#fff"/>
    <ellipse cx="546" cy="460" rx="142" ry="134" fill="url(#towerTone)" role="img" aria-label="Photo of a launch pad service tower on a hill under a pale blue sky"/>
  </svg>

  <section class="capabilities">
    <p class="capability">Q7 Strata personnel have been at the forefront of major program deliveries to Defence and Commercial sector clients for decades. Our staff are leaders in their field and pioneers in the establishment of systematic approaches to the most complex problems.</p>
    <p class="capability">With access to skilled personnel locally and internationally, Q7 Strata can review, de-risk, and support delivery of space orientated systems and services.</p>
    <p class="capability">Q7 Strata is supported by engineers with capabilities in the design and development of rocket systems and expertise in RF SATCOM communications technologies.</p>
    <p class="capability">We understand rocket systems from work on missile and UAV development and trials at Woomera, Jervis Bay, RAN ships, and Port Wakefield test range.</p>
    <p class="capability">We understand the complexity associated with launch facilities, rocket launch, and recovery operations for rocket propelled systems and associated technologies.</p>
    <p class="capability">We understand cybersecurity technologies, communications, systems engineering, systems design, facilities, integration, infrastructure, and modern systems development principles.</p>
    <p class="capability">And by understanding, we are in the best position to support our customer requirements and business needs.</p>
    <p class="capability">With prior work on multi-billion-dollar programs of tactical and strategic importance to the country, we can directly support the Space sector in education, research and technology development that helps grow the broader community interest in space.</p>
  </section>

  <h2 class="recruit-heading">Are you living outside of Australia and want to work within Australia’s dynamic and evolving Space sector?</h2>
  <div class="recruit-rule"></div>

  <section class="recruit-body">
    <p>Q7 Strata provides a streamlined process, support services, and employment options to suitably qualified people who are seeking work within Space in Australia.</p>
    <p>Our transition plans include flexible employment options, relocation services to accommodate your needs, remote work options, ongoing assistance, and valuable local information to empower you to navigate your time in Australia with ease.</p>
  </section>

  <section class="mission">
    <p>Our mission is to bring exceptional talent into the Australian Space sector and offer a quality experience that is both enjoyable and rewarding.</p>
    <p>If you’re an experienced Space professional seeking to work within Australia, contact us at</p>
    <p class="mission-email">enquiries@q7strata-demo.com.au</p>
  </section>

  <h1 class="tagline">
    <span class="tagline-light">A trusted provider</span>
    <span class="tagline-bold">to the world’s most exacting clients</span>
  </h1>

  <div class="base-band"></div>
</main>
</body>
</html>
```